Coaching business needs flyer for business market

I need a flyer that I can send to HR-managers and business owners to inform them of my coaching services for organisations. We have three services: organisational- and teamcoaching, individual coaching and training programs.
I want the flyer to express calmness, solid and trustworthy coaching. As a person I am open and think out of the box.

In my logo I use a couple of colours (blue, green, orange and grey) that represent the diversity of humans. My company's name is Bramblecrest Engagement & Coaching and tag line is "Awaken your quiet river".

I do not want the design to be too busy but also not too boring. I tried making something myself. Feel free to build on that design. Or feel free to start from scratch.

```html
<!DOCTYPE html>
<html lang="nl">
<head>
<meta charset="utf-8">
<title>Bramblecrest Engagement &amp; Coaching – Flyer</title>
<link href="https://fonts.googleapis.com/css2?family=Montserrat:wght@400;500;600;700&family=Poppins:wght@700;800&family=Dancing+Script:wght@700&family=Caveat:wght@500&display=swap" rel="stylesheet">
<style>
:root{
  --orange:#f39a1e;
  --blue:#2f5f8a;
  --red:#c93c2a;
  --teal:#6aada6;
  --teal-light:#bce3e0;
  --teal-dark:#1f7b74;
  --band:#3a6795;
  --ink:#2b2b2b;
  --backdrop:#8f8c8c;
}
*{margin:0;padding:0;box-sizing:border-box}
html,body{width:971px;height:1200px;overflow:hidden}
body{background:var(--backdrop);font-family:"Montserrat",sans-serif;color:var(--ink);position:relative}
.flyer{position:absolute;left:105px;top:94px;width:774px;height:1002px;background:linear-gradient(#fff 60%,#f1f6f5);overflow:hidden}
.colour-bar{position:absolute;left:0;width:774px;height:7px}
.colour-bar span{position:absolute;top:0;height:7px}
.colour-bar .c1{left:0;width:115px;background:var(--orange)}
.colour-bar .c2{left:119px;width:159px;background:var(--blue)}
.colour-bar .c3{left:282px;width:172px;background:var(--red)}
.colour-bar .c4{left:458px;width:160px;background:var(--teal)}
.colour-bar .c5{left:621px;width:153px;background:var(--blue)}
.bar-top{top:0}
.bar-bottom{top:754px}

.portrait{position:absolute;left:40px;top:43px;width:300px;height:304px;border-radius:17px 17px 0 0;background:radial-gradient(circle at 55% 45%,#8a6650 0 28%,#5b9e98 29% 100%)}
.bio-panel{position:absolute;left:40px;top:347px;width:300px;height:407px;background:var(--teal-light)}
.quote-mark{position:absolute;left:24px;top:-8px;font-family:Georgia,serif;font-size:170px;line-height:1;color:#9dd0ca;font-weight:700}
.coach-name{position:absolute;left:27px;top:88px;font-family:"Dancing Script",cursive;font-size:32px;color:var(--teal-dark);white-space:nowrap}
.bio{position:absolute;left:27px;top:137px;width:250px;font-size:12.6px;line-height:15.05px;color:#333;letter-spacing:-.15px}

.service-frames{position:absolute;left:0;top:0}
.tail{position:absolute;left:403px;width:60px;border-radius:0 0 0 16px;background:linear-gradient(#fff,#e4e4e4)}
.photo-ring{position:absolute;left:366px;width:150px;height:150px;border-radius:50%;background:#fff;border:3px solid}
.photo-ring .photo{position:absolute;inset:6px;border-radius:50%}
.ring-red{top:49px;border-color:var(--red)}
.ring-blue{top:281px;border-color:var(--blue)}
.ring-orange{top:530px;border-color:var(--orange)}
.photo-team{background:radial-gradient(circle at 50% 60%,#8a7a6e,#c9b9a6 70%)}
.photo-individual{background:radial-gradient(circle at 50% 55%,#555,#d9d2c4 65%)}
.photo-training{background:radial-gradient(circle at 50% 45%,#6f7f8f,#1d1d24 70%)}

.service-title{position:absolute;left:530px;font-family:"Poppins",sans-serif;font-weight:800;font-size:16.6px;line-height:20px;letter-spacing:-.2px;background:#fff;padding-right:6px}
.title-team{top:53px;color:var(--red)}
.title-individual{top:303px;color:var(--blue)}
.title-training{top:551px;color:var(--orange)}

.service-list{position:absolute;left:531px;list-style:none;font-size:10.6px;line-height:13.4px;color:#333}
.service-list li{position:relative;padding-left:25px;margin-bottom:6px}
.q{position:absolute;left:0;top:2px;width:20px;height:20px;border-radius:50%;color:#fff;font-weight:700;font-size:13px;line-height:20px;text-align:center;box-shadow:0 0 0 2px #fff,0 0 0 3px currentColor}
.list-team{top:99px}
.list-team .q{background:var(--red);color:#fff;box-shadow:0 0 0 2px #fff,0 0 0 3px #e7a79c}
.list-individual{top:331px}
.list-individual .q{background:var(--blue);box-shadow:0 0 0 2px #fff,0 0 0 3px #9bb3cb}
.list-training{top:584px}
.list-training li{margin-bottom:8px}
.list-training svg{position:absolute;left:5px;top:0}

.results-band{position:absolute;left:0;top:766px;width:774px;height:236px;background:linear-gradient(100deg,#3c6a98,#34608f 60%,#3b6a97)}
.headline{position:absolute;left:0;width:774px;top:20px;text-align:center;font-family:"Poppins",sans-serif;font-weight:700;font-size:22px;color:#fff;letter-spacing:-.4px;padding-right:30px}
.headline-script{position:absolute;left:0;width:774px;top:42px;text-align:center;font-family:"Caveat",cursive;font-size:40px;color:var(--orange)}
.methods{position:absolute;left:46px;top:104px;list-style:none;color:#fff;font-weight:700;font-size:13.4px;line-height:18px;width:520px}
.methods li{position:relative;padding-left:19px;margin-bottom:4.5px}
.methods svg{position:absolute;left:0;top:3px}
.brand{position:absolute;left:580px;top:94px;width:180px;text-align:center;color:#fff}
.brand-dot{width:54px;height:54px;border-radius:50%;border:2px solid #fff;margin:0 auto 12px}
.brand-name{font-family:"Montserrat",sans-serif;font-weight:500;font-size:15px;line-height:19px}
</style>
</head>
<body>
<main class="flyer">
  <div class="colour-bar bar-top"><span class="c1"></span><span class="c2"></span><span class="c3"></span><span class="c4"></span><span class="c5"></span></div>

  <div class="portrait" role="img" aria-label="Portret van de coach, lachend, tegen een tealkleurige achtergrond"></div>
  <section class="bio-panel">
    <div class="quote-mark">“</div>
    <h1 class="coach-name">Marisol Dekker</h1>
    <p class="bio">is trainer en coach. Ze heeft ruime ervaring met veranderingstrajecten binnen organisaties. Mensen omschrijven haar als ‘betrokken, warm, stevig en kordaat’. Het is haar passie om organisaties, teams en mensen te helpen groeien. Zij helpt weerstand te overwinnen en draagt bij aan groei in zelfvertrouwen. Haar trainingen en coaching zijn erop gericht om snel inzichtelijk te krijgen welke stappen men moet zetten om verder te komen. Ze gelooft de veranderkracht van de mensen waar ze mee werkt.<br>Ze is er om steun en richting te bieden en laat hen zelf aan het roer.</p>
  </section>

  <div class="tail" style="top:190px;height:62px"></div>
  <div class="tail" style="top:420px;height:83px"></div>
  <div class="tail" style="top:670px;height:45px"></div>

  <svg class="service-frames" width="774" height="760" viewBox="0 0 774 760" fill="none" stroke-width="2">
    <path d="M676 82 H724 A18 18 0 0 1 742 100 V241 A18 18 0 0 1 724 259 H414 A18 18 0 0 1 396 241 V190" stroke="#c93c2a"/>
    <path d="M728 313 A14 14 0 0 1 742 327 V490 A18 18 0 0 1 724 508 H414 A18 18 0 0 1 396 490 V420" stroke="#2f5f8a"/>
    <path d="M718 561 H726 A16 16 0 0 1 742 577 V702 A18 18 0 0 1 724 720 H414 A18 18 0 0 1 396 702 V660" stroke="#f39a1e"/>
  </svg>

  <div class="photo-ring ring-red"><div class="photo photo-team" role="img" aria-label="Teamsessie met deelnemers staand in een ruimte"></div></div>
  <div class="photo-ring ring-blue"><div class="photo photo-individual" role="img" aria-label="Individuele coachsessie in een lichte kamer"></div></div>
  <div class="photo-ring ring-orange"><div class="photo photo-training" role="img" aria-label="Training met groep in een zaal met banner"></div></div>

  <h2 class="service-title title-team">ORGANISATIONAL AND<br>TEAMCOACHING</h2>
  <ul class="service-list list-team">
    <li><span class="q">?</span>Heb je zorgen voor of na een<br>fusie of verandering?</li>
    <li><span class="q">?</span>Wil je missie, visie &amp; strategie<br>ontwikkelen of wijzigen?</li>
    <li><span class="q">?</span>Wens je de cultuur-veranderen<br>of verder ontwikkelen?</li>
    <li><span class="q">?</span>Beoog je de samenwerking<br>bevorderen of verbeteren?</li>
  </ul>

  <h2 class="service-title title-individual">INDIVIDUAL COACHING</h2>
  <ul class="service-list list-individual">
    <li><span class="q">?</span>Wens je medewerkers die hun<br>talent ten volste benutten?</li>
    <li><span class="q">?</span>Verlang je meer authentieke<br>leiderschap bij je collega’s?</li>
    <li><span class="q">?</span>Wil je de mensen vooruit helpen<br>in hun loopbaan?</li>
    <li><span class="q">?</span>Zoek je steun voor medewerkers<br>met burn-out of re-integratie?</li>
    <li><span class="q">?</span>Heb je hulp nodig bij<br>outplacement trajecten?</li>
  </ul>

  <h2 class="service-title title-training">TRAINING PROGRAMS</h2>
  <ul class="service-list list-training">
    <li><svg width="14" height="14" viewBox="0 0 14 14" fill="none" stroke="#f39a1e" stroke-width="1.5"><path d="M12 6.5 A5.5 5.5 0 1 1 9 2"/><path d="M4 7 L6.5 9.5 L13 2.5"/></svg>Leiderschap</li>
    <li><svg width="14" height="14" viewBox="0 0 14 14" fill="none" stroke="#f39a1e" stroke-width="1.5"><path d="M12 6.5 A5.5 5.5 0 1 1 9 2"/><path d="M4 7 L6.5 9.5 L13 2.5"/></svg>Communicatie</li>
    <li><svg width="14" height="14" viewBox="0 0 14 14" fill="none" stroke="#f39a1e" stroke-width="1.5"><path d="M12 6.5 A5.5 5.5 0 1 1 9 2"/><path d="M4 7 L6.5 9.5 L13 2.5"/></svg>Leren kijken met ‘systemische<br>blik’ voor professionals</li>
    <li><svg width="14" height="14" viewBox="0 0 14 14" fill="none" stroke="#f39a1e" stroke-width="1.5"><path d="M12 6.5 A5.5 5.5 0 1 1 9 2"/><path d="M4 7 L6.5 9.5 L13 2.5"/></svg>Conflicthantering</li>
  </ul>

  <div class="colour-bar bar-bottom"><span class="c1"></span><span class="c2"></span><span class="c3"></span><span class="c4"></span><span class="c5"></span></div>

  <section class="results-band" role="img" aria-label="Blauw getinte foto van een groepssessie als achtergrond">
    <h2 class="headline">Gedegen resultaat en kwaliteit door bewezen</h2>
    <p class="headline-script">‘best practices’</p>
    <ul class="methods">
      <li><svg width="13" height="13" viewBox="0 0 14 14" fill="none" stroke="#fff" stroke-width="1.5"><path d="M12 6.5 A5.5 5.5 0 1 1 9 2"/><path d="M4 7 L6.5 9.5 L13 2.5"/></svg>Neuro Linguïstisch Programmeren (NLP)</li>
      <li><svg width="13" height="13" viewBox="0 0 14 14" fill="none" stroke="#fff" stroke-width="1.5"><path d="M12 6.5 A5.5 5.5 0 1 1 9 2"/><path d="M4 7 L6.5 9.5 L13 2.5"/></svg>Transactionele Analyse</li>
      <li><svg width="13" height="13" viewBox="0 0 14 14" fill="none" stroke="#fff" stroke-width="1.5"><path d="M12 6.5 A5.5 5.5 0 1 1 9 2"/><path d="M4 7 L6.5 9.5 L13 2.5"/></svg>Systemisch Werken: Organisatieopstellingen, Familieopstellingen, Identity oriented Psycho Traumaopstellingen)</li>
      <li><svg width="13" height="13" viewBox="0 0 14 14" fill="none" stroke="#fff" stroke-width="1.5"><path d="M12 6.5 A5.5 5.5 0 1 1 9 2"/><path d="M4 7 L6.5 9.5 L13 2.5"/></svg>Somatic Experience, Ademwerk en Lichaamswerk</li>
    </ul>
    <div class="brand">
      <div class="brand-dot"></div>
      <p class="brand-name">Bramblecrest<br>Engagement &amp; Coaching</p>
    </div>
  </section>
</main>
</body>
</html>
```